Three diagrams for an academic paper

I need professional-looking versions of three diagrams for an academic paper. I am uploading JPEGs of each diagram drafted in Google Docs. I need completely new versions that look much better.

Some detailed requirements:
- Professional styling - must be clearly superior to the ‘stick-figure’ example images and obviously not from powerpoint, etc.
- Must be a coordinated style across all three illustrations.
- Note that a mini-version of figure 2 appears in figure 3 (within the database image)
- I need very high resolution, suitable for a manuscript
- May need some text changes at short notice (anticipate 2 small updates to text)

Target Market(s)

Academics

Industry/Entity Type

Google

Font styles to use
Sans Serif

Colors

Requirements
Must have
• Don't look like powerpoint

```html
<!DOCTYPE html>
<html lang="en">
<head>
<meta charset="utf-8">
<title>Database of Structured Journalistic Knowledge</title>
<link href="https://fonts.googleapis.com/css2?family=Arimo:wght@400;700&family=Roboto+Mono:wght@500&display=swap" rel="stylesheet">
<style>
  :root{
    --bg:#ffffff;
    --ink:#4a4a4a;
    --panel:#f0f0f0;
    --connector:#ebebeb;
    --sky:#6ac1e6;
    --steel:#3f7898;
    --teal:#5fd3dc;
    --navy:#1a4d74;
    --frame-top:#45c6d6;
    --frame-bottom:#1b4e74;
  }
  html,body{margin:0;padding:0;overflow:hidden;background:var(--bg);}
  .canvas{position:relative;width:1200px;height:1200px;overflow:hidden;background:var(--bg);font-family:"Arimo",Arial,sans-serif;color:var(--ink);}
  .wires{position:absolute;left:0;top:0;}
  .heading{position:absolute;top:304px;margin:0;font-size:32px;font-weight:700;letter-spacing:-.3px;line-height:40px;}
  .heading--sources{left:32px;color:var(--sky);}
  .heading--products{right:30px;color:var(--steel);}
  .item{position:absolute;height:53px;display:flex;align-items:center;justify-content:center;text-align:center;font-weight:700;font-size:17px;line-height:22px;}
  .source{left:30px;width:264px;background:var(--panel);clip-path:polygon(0 0,calc(100% - 15px) 0,100% 50%,calc(100% - 15px) 100%,0 100%);padding-left:18px;padding-right:12px;box-sizing:border-box;}
  .source::before{content:"";position:absolute;left:0;top:0;width:18px;height:100%;background:var(--sky);}
  .product{left:870px;width:300px;background:var(--panel);clip-path:polygon(15px 0,100% 0,100% 100%,15px 100%,0 50%);padding-left:14px;padding-right:18px;box-sizing:border-box;}
  .product::after{content:"";position:absolute;right:0;top:0;width:18px;height:100%;background:var(--steel);}
  .legend{position:absolute;left:493px;top:186px;margin:0;padding:0;list-style:none;font-weight:700;font-size:17px;}
  .legend li{display:flex;align-items:center;height:24px;margin-bottom:10px;}
  .legend .dot{width:19px;height:19px;border-radius:50%;margin-right:11px;}
  .dot--text{background:var(--teal);} .dot--data{background:var(--navy);}
  .store-panel{position:absolute;left:486px;width:191px;background:var(--panel);}
  .prose,.data,.slot{position:absolute;box-sizing:border-box;}
  .prose{left:10px;width:69px;background:var(--teal) repeating-linear-gradient(to bottom,transparent 0 6px,#fff 6px 7px,transparent 7px 10.4px);background-clip:content-box;padding:3px 8px;background-color:var(--teal);}
  .prose{background:repeating-linear-gradient(to bottom,var(--teal) 0 6px,#ffffff 6px 7px,var(--teal) 7px 10.4px);border:0 solid var(--teal);border-width:3px 8px;}
  .data{left:87px;width:95px;background:var(--navy);color:#fff;font-family:"Roboto Mono",monospace;font-size:9.6px;line-height:15.4px;padding:3px 0 0 7px;letter-spacing:.4px;}
  .slot{border:1.5px dashed;}
  .slot--data{left:86px;width:96px;border-color:var(--navy);}
  .slot--prose{left:10px;width:69px;border-color:var(--teal);}
  .axis{position:absolute;font-weight:700;font-size:20px;letter-spacing:.3px;white-space:nowrap;transform:translate(-50%,-50%) rotate(-90deg);}
  .store-title{position:absolute;left:381px;top:962px;width:400px;margin:0;text-align:center;font-weight:700;font-size:20px;line-height:25px;letter-spacing:.3px;}
</style>
</head>
<body>
<main class="canvas">
  <svg class="wires" width="1200" height="1200" viewBox="0 0 1200 1200" aria-hidden="true">
    <defs>
      <linearGradient id="frameStroke" x1="0" y1="0" x2="0" y2="1">
        <stop offset="0" stop-color="var(--frame-top)"/>
        <stop offset="0.55" stop-color="#3aa9d6"/>
        <stop offset="1" stop-color="var(--frame-bottom)"/>
      </linearGradient>
    </defs>
    <g fill="none" stroke="#ebebeb" stroke-width="2.5" stroke-linejoin="round" stroke-linecap="round">
      <path d="M294 386 H376 L436 414 M428 406 L437 414 L426 419"/>
      <path d="M294 465 H376 L436 490 M427 483 L437 490 L426 496"/>
      <path d="M294 543 H376 L436 572 M428 563 L437 572 L426 577"/>
      <path d="M294 621 H436 M428 614 L437 621 L428 628"/>
      <path d="M294 699 H376 L436 672 M426 668 L437 672 L428 681"/>
      <path d="M294 778 H376 L436 755 M426 750 L437 755 L428 764"/>
      <path d="M294 856 H376 L436 832 M426 827 L437 832 L428 841"/>
      <path d="M722 621 L800 386 H866 M858 378 L867 386 L858 394"/>
      <path d="M722 621 L800 465 H866 M858 457 L867 465 L858 473"/>
      <path d="M722 621 L800 543 H866 M858 535 L867 543 L858 551"/>
      <path d="M722 621 H866 M858 613 L867 621 L858 629"/>
      <path d="M722 621 L800 699 H866 M858 691 L867 699 L858 707"/>
      <path d="M722 621 L800 778 H866 M858 770 L867 778 L858 786"/>
      <path d="M722 621 L800 856 H866 M858 848 L867 856 L858 864"/>
    </g>
    <rect x="440" y="263" width="280" height="683" rx="10" fill="none" stroke="url(#frameStroke)" stroke-width="3.5"/>
    <path d="M713 434 L720 426 L727 434" fill="none" stroke="#45c6d6" stroke-width="3" stroke-linecap="round"/>
    <path d="M433 798 L440 806 L447 798" fill="none" stroke="#2d6c95" stroke-width="3" stroke-linecap="round"/>
  </svg>

  <h2 class="heading heading--sources">DATA SOURCES</h2>
  <h2 class="heading heading--products">NEWS PRODUCTS</h2>

  <div class="item source" style="top:360px">Sencors</div>
  <div class="item source" style="top:438px">Existing Datasets</div>
  <div class="item source" style="top:517px">Manual Data Entry</div>
  <div class="item source" style="top:594px">Manual Annotation<br>of Text</div>
  <div class="item source" style="top:673px">Controlled Natural<br>Language Authoring</div>
  <div class="item source" style="top:751px">Automated Annotation<br>of Text</div>
  <div class="item source" style="top:830px">Automated Data<br>Extraction or Assembly</div>

  <div class="item product" style="top:360px">Conversational Interfaces<br>(News Bots)</div>
  <div class="item product" style="top:438px">Automatically Written<br>Articles</div>
  <div class="item product" style="top:518px">Authored Articles<br>(via Analysis)</div>
  <div class="item product" style="top:594px">Graphics and<br>Visualisations</div>
  <div class="item product" style="top:673px">Texteme-Based News<br>Products (cars, etc)</div>
  <div class="item product" style="top:751px">Quantitative News<br>Products (totals, tabels)</div>
  <div class="item product" style="top:829px">Other Computable<br>News Products</div>

  <ul class="legend">
    <li><span class="dot dot--text"></span>Natural language</li>
    <li><span class="dot dot--data"></span>Structured data</li>
  </ul>

  <section class="store" aria-label="Database of structured journalistic knowledge">
    <div class="store-panel" style="top:290px;height:162px">
      <div class="prose" style="top:10px;height:142px"></div>
      <div class="slot slot--data" style="top:10px;height:65px"></div>
    </div>
    <div class="store-panel" style="top:466px;height:161px">
      <div class="prose" style="top:9px;height:143px"></div>
      <div class="data" style="top:9px;height:65px">101010110010<br>111001100110<br>000101101101<br>10110</div>
    </div>
    <div class="store-panel" style="top:646px;height:111px">
      <div class="prose" style="top:1px;height:103px"></div>
      <div class="data" style="top:1px;height:51px">101010110010<br>111001100110<br>000101101101</div>
    </div>
    <div class="store-panel" style="top:767px;height:70px">
      <div class="prose" style="top:9px;height:31px"></div>
      <div class="data" style="top:9px;height:51px">101010110010<br>111001100110<br>000101101101</div>
    </div>
    <div class="store-panel" style="top:849px;height:69px">
      <div class="slot slot--prose" style="top:9px;height:52px"></div>
      <div class="data" style="top:9px;height:51px">101010110010<br>111001100110<br>000101101101</div>
    </div>
    <span class="axis" style="left:465px;top:606px">MORE STRUCTURE</span>
    <span class="axis" style="left:696px;top:606px">LESS STRUCTURE</span>
  </section>

  <p class="store-title">DATABASE OF STRUCTURED<br>JOURNALISTIC KNOWLEDGE</p>
</main>
</body>
</html>
```